We are growing our coaching practice and need some help creating collateral

Our organisation is building a coaching practice. It's going well and we want to take it to the next level. To date, we've done our own basic marketing material (attached), but now we want to create something more substantial that captures our approach and gives us confidence and pride when talking to customers. Things to note - we aren't looking for logo design, that's a separate branding discussion in our organisation. We are looking for someone to take our existing content and make it look good - this might be in the form of a flyer or PPT slide deck for example.
The format we are looking for is the offering title - in this case, 'Coaching', a brief description, and then some further detail.
Target Market(s)
Corporate, Healthcare, IT
Colors
Designer to choose colors to be used in the design.
Look and feel
Each slider illustrates characteristics of the customer's brand and the style your logo design should communicate.

```html
<!DOCTYPE html>
<html lang="en">
<head>
<meta charset="utf-8">
<title>Nexa Executive Coaching</title>
<link href="https://fonts.googleapis.com/css2?family=Oswald:wght@500;700&family=Raleway:wght@800&family=Open+Sans:wght@400;700&display=swap" rel="stylesheet">
<style>
  :root{
    --orange:#f9a51d;
    --red-hot:#e2532a;
    --red-deep:#8e1d18;
    --red-brand:#b3261e;
    --ink:#2b2b2b;
    --charcoal:#1a1a1a;
    --white:#ffffff;
  }
  html,body{margin:0;padding:0;overflow:hidden;background:#fff}
  .flyer{position:relative;width:927px;height:1200px;overflow:hidden;font-family:"Open Sans",sans-serif;color:var(--white)}
  .backdrop{position:absolute;inset:0}
  .block{position:absolute;margin:0}
  .body-text{font-size:13.6px;line-height:21.2px;margin:0 0 12px}
  .section-title{font-family:"Raleway",sans-serif;font-weight:800;font-size:34px;line-height:34px;margin:0}
  .brand{position:absolute;left:24px;top:18px;display:flex;align-items:center;gap:18px}
  .brand-name{font-family:"Oswald",sans-serif;font-weight:700;font-size:64px;line-height:80px;color:var(--red-brand)}
  .brand-tag{font-family:"Oswald",sans-serif;font-weight:500;font-size:31px;line-height:34px;color:var(--ink);letter-spacing:1px}
  .coaches{left:24px;top:262px;width:530px}
  .coaches .section-title{display:inline;margin-right:8px}
  .meet{left:24px;top:484px;width:530px}
  .meet .section-title{margin-bottom:4px}
  .credentials-title{font-size:13.6px;letter-spacing:1.6px;margin:2px 0 6px}
  .credentials{list-style:none;padding:0;margin:0;font-size:13.6px;line-height:21.2px}
  .credentials li{padding-left:9px;text-indent:-9px}
  .credentials li::before{content:"• "}
  .believe{left:630px;top:64px;width:276px}
  .packages{left:627px;top:376px;width:276px}
  .believe .section-title,.packages .section-title{margin-bottom:0}
  .cta{position:absolute;right:33px;top:1026px;text-align:right}
  .cta-lead{font-family:"Oswald",sans-serif;font-weight:500;font-size:27px;line-height:33.5px;color:var(--ink);margin:0;text-transform:uppercase}
  .cta-lead em{font-style:normal;color:var(--red-brand)}
  .cta-contact{font-weight:700;font-size:19px;line-height:28px;color:#3a3a3a;margin:4px 0 0}
</style>
</head>
<body>
<div class="flyer">
  <svg class="backdrop" width="927" height="1200" viewBox="0 0 927 1200" aria-hidden="true">
    <defs>
      <radialGradient id="redGlow" cx="0.42" cy="0.45" r="0.7">
        <stop offset="0" stop-color="#e2532a"/>
        <stop offset="0.55" stop-color="#b52a1f"/>
        <stop offset="1" stop-color="#5a1410"/>
      </radialGradient>
      <linearGradient id="darkPanel" x1="0" y1="0" x2="0.3" y2="1">
        <stop offset="0" stop-color="#050505"/>
        <stop offset="1" stop-color="#4a4a4a"/>
      </linearGradient>
      <linearGradient id="silver" x1="0" y1="0" x2="1" y2="0">
        <stop offset="0" stop-color="#d6d6d6"/>
        <stop offset="0.35" stop-color="#8d8d8d"/>
        <stop offset="0.55" stop-color="#e8e8e8"/>
        <stop offset="0.8" stop-color="#9a9a9a"/>
        <stop offset="1" stop-color="#dcdcdc"/>
      </linearGradient>
    </defs>
    <rect width="927" height="1200" fill="url(#redGlow)"/>
    <polygon points="560,0 927,0 927,900 636,944" fill="url(#darkPanel)"/>
    <polygon points="0,0 624,0 0,216" fill="var(--orange)"/>
    <polygon points="624,0 752,0 0,268 0,216" fill="url(#silver)"/>
    <polygon points="0,1040 927,894 927,946 0,1094" fill="url(#silver)"/>
    <polygon points="0,1094 927,946 927,1200 0,1200" fill="var(--orange)"/>
  </svg>

  <header class="brand">
    <span class="brand-name">NEXA</span>
    <span class="brand-tag">EXECUTIVE<br>COACHING</span>
  </header>

  <section class="block coaches">
    <p class="body-text"><span class="section-title">OUR COACHES</span> are highly attuned to the human systems within which you work and live, since understanding those interconnected forces is vital to unlock movement. We build on your existing strengths and seek sustainable shifts, ones that create ripple effects of positive change.</p>
    <p class="body-text">Leaders everywhere face unprecedented change, pressure, ambiguity, culture and accountability dilemmas. And yet every leader also has a different story, different terrain to navigate and different aspirations. This is where executive coaching with Nexa can create extraordinary results.</p>
  </section>

  <section class="block meet">
    <h2 class="section-title">MEET ONE OF OUR COACHES</h2>
    <p class="body-text">Sam Porter leads the Executive Coaching practice for Nexa across Australia and New Zealand.</p>
    <p class="body-text">He has worked at senior levels in the ACT Public Service, the Australian Public Service and in the private sector. His continuing focus over the past 20 years has been on organizational and people development. As a Masters-qualified and highly experienced executive coach, Sam's passion lies in unlocking human potential. He has coached doctors, nurses, allied health clinicians, statisticians, scientists, educators, IT professionals, Senior managers and Executives in the APS (EL1 – SES), ACT Government (SOGC – Executive bands) and private sector.</p>
    <p class="body-text">When Sam is not coaching, he is facilitating workshops and consulting to enable teams and organizations to make effective transformations.</p>
    <h3 class="credentials-title">QUALIFICATIONS, ACCREDITATIONS, MEMBERSHIPS:</h3>
    <ul class="credentials">
      <li>Master of Science in Coaching Psychology</li>
      <li>Graduate Certificate in Management</li>
      <li>Certificate IV in Workplace Assessment &amp; Training</li>
      <li>Style Inventory Accreditation, Culture Metrics</li>
      <li>Type Profile Accreditation</li>
      <li>Member, Global Coaching Guild (GCG)</li>
      <li>Member, Harbour University Coaching<br>&amp; Mentoring Alumni Association.</li>
    </ul>
  </section>

  <section class="block believe">
    <h2 class="section-title">WE BELIEVE</h2>
    <p class="body-text">great coaching is a bridge: one that enables you to see more clearly and cross the unexpected chasms; one that supports and challenges your thinking and actions to progress your significant goals.</p>
    <p class="body-text">We build a creative and confidential partnership with you, one that is grounded in the science of leadership, change and coaching psychology so that practical results are an expectation and not left to chance.</p>
  </section>

  <section class="block packages">
    <h2 class="section-title">OUR PACKAGES</h2>
    <p class="body-text">typically consist of blocks of 7 hourly sessions, conducted fortnightly (with flexibility to customize).</p>
    <p class="body-text">For EL2 leaders, the investment in a block of 7 sessions is $3400 + GST. This includes significant preparation and conceptualization time before and after sessions by your coach to ensure you achieve maximum value.</p>
  </section>

  <footer class="cta">
    <p class="cta-lead">Why not explore the possibilities executive<br>coaching offers through a <em>no obligation initial session,</em><br>ensuring the approach and the coach is a good fit for you?</p>
    <p class="cta-contact">Contact Sam Porter, ph. 0400 000 000, sam.porter@nexacoaching.com<br>For details on other Nexa services please visit www.nexacoaching.com</p>
  </footer>
</div>
</body>
</html>
```